PowerPoint template for project mangement course material

I need a ppt template for the slides at our project management course. IT should be arather simple adn stylish not taking the focus away from the content. We are two companies delivering the course - thus the template should be held in the colours of the two companies and their logos. we need different layouts for the template - the logos should be included in minimum the title layout.
The content is a mix of text and figures.
(uploaded ppt shows an example of the content)

Industry/Entity Type

Training

Font styles to use
Serif
Sans Serif

Requirements
Must have
• different layouts: title, section, standard, two columns, headline only etc.
Nice to have
• nice bullets, mostly white background

```html
<!DOCTYPE html>
<html lang="da">
<head>
<meta charset="utf-8">
<title>Projektledelse Praksis – slide template</title>
<link rel="stylesheet" href="https://fonts.googleapis.com/css2?family=Raleway:wght@200;300;600;700&display=swap">
<style>
  :root {
    --page: #ffffff;
    --stage: #636363;
    --red: #a84c4c;
    --blue: #3e5a82;
    --ink: #2b2b2b;
    --muted: #6a6a6a;
    --slide: #ffffff;
  }
  * { margin: 0; padding: 0; box-sizing: border-box; }
  html, body { width: 1200px; height: 675px; overflow: hidden; background: var(--page); }
  body { font-family: "Raleway", Arial, sans-serif; color: var(--ink); position: relative; }

  .stage { position: absolute; left: 47px; top: 209px; width: 1106px; height: 257px; background: var(--stage); }

  .slide { position: absolute; top: 273px; width: 245px; height: 138px; background: var(--slide); overflow: hidden; box-shadow: 0 0 0 1px rgba(0,0,0,.15); }
  .slide--title { left: 53px; }
  .slide--welcome { left: 303px; }
  .slide--purpose { left: 597px; }
  .slide--section { left: 849px; }

  /* Title slide */
  .partner { position: absolute; top: 17px; display: flex; align-items: center; gap: 3px; font-size: 5px; font-weight: 600; color: var(--muted); }
  .partner--left { left: 2px; }
  .partner--right { right: 2px; }
  .partner__mark { width: 5px; height: 5px; }
  .title-block { position: absolute; left: 0; right: 0; top: 56px; text-align: center; }
  .title-block__head { font-size: 7px; font-weight: 700; letter-spacing: .3px; }
  .title-block__head .red { color: var(--red); }
  .title-block__head .blue { color: var(--blue); margin-left: 3px; }
  .title-block__sub { font-size: 3.6px; color: var(--muted); margin-top: 3px; line-height: 1.5; }
  .title-band { position: absolute; left: 0; right: 0; bottom: 0; height: 14px;
    background: linear-gradient(90deg, var(--blue) 0%, #7d8aa0 50%, var(--red) 100%); }
  .title-band::after { content: ""; position: absolute; left: 0; right: 0; top: 5px; height: 3px;
    background: linear-gradient(90deg, var(--red), var(--blue)); opacity: .6; }

  /* Welcome slide */
  .welcome__photo { position: absolute; inset: 0; background: linear-gradient(180deg, #8e6266 0%, #6f5a62 55%, #4d5670 100%); }
  .welcome__word { position: absolute; left: 0; right: 0; top: 66px; text-align: center; color: #fff; font-weight: 200; font-size: 11px; letter-spacing: .2px; }
  .marker { position: absolute; width: 6px; height: 6px; }

  /* Purpose slide */
  .purpose__title { position: absolute; left: 42px; top: 40px; font-size: 11px; font-weight: 200; letter-spacing: .2px; white-space: nowrap; }
  .purpose__text { position: absolute; left: 12px; font-size: 3.4px; color: var(--ink); white-space: nowrap; }
  .purpose__rule { position: absolute; left: 12px; top: 91px; width: 4px; height: 0.5px; background: var(--ink); }
  .purpose__strip { position: absolute; right: 0; top: 0; bottom: 0; width: 49px; background: linear-gradient(180deg, var(--red), var(--blue)); }

  /* Section slide */
  .section__frame { position: absolute; inset: 0; }
  .section__title { position: absolute; left: 41px; top: 95px; font-size: 11px; font-weight: 200; letter-spacing: .2px; white-space: nowrap; }
</style>
</head>
<body>
  <div class="stage"></div>

  <section class="slide slide--title">
    <div class="partner partner--left">
      <svg class="partner__mark" viewBox="0 0 10 10"><path d="M0 2h5V0l5 5-5 5V8H0z" fill="var(--red)"/></svg>
      <span>Nordvik Akademi</span>
    </div>
    <div class="partner partner--right">
      <span>Askeby</span>
      <svg class="partner__mark" viewBox="0 0 10 10"><path d="M10 2H5V0L0 5l5 5V8h5z" fill="var(--blue)"/></svg>
    </div>
    <div class="title-block">
      <div class="title-block__head"><span class="red">PROJEKTLEDELSE</span><span class="blue">PRAKSIS</span></div>
      <div class="title-block__sub">Modul 1 – introduktion og overblik<br>Dag 1</div>
    </div>
    <div class="title-band"></div>
  </section>

  <section class="slide slide--welcome">
    <div class="welcome__photo" role="img" aria-label="Tinted street photo with a truck carrying a road-to-success slogan"></div>
    <svg class="marker" style="left:94px;top:58px" viewBox="0 0 10 10"><path d="M1 1h8L5 9z" fill="#fff"/></svg>
    <div class="welcome__word">VELKOMMEN</div>
    <svg class="marker" style="left:160px;top:80px" viewBox="0 0 10 10"><path d="M5 1l4 8H1z" fill="#fff"/></svg>
  </section>

  <section class="slide slide--purpose">
    <svg class="marker" style="left:42px;top:31px" viewBox="0 0 10 10"><path d="M1 1h8L5 9z" fill="var(--blue)"/></svg>
    <div class="purpose__title">FORMÅL MED KURSET</div>
    <svg class="marker" style="left:156px;top:54px" viewBox="0 0 10 10"><path d="M5 1l4 8H1z" fill="var(--red)"/></svg>
    <p class="purpose__text" style="top:77px">At give deltagerne et godt fundament for at planlægge og styre egne projekter</p>
    <div class="purpose__rule"></div>
    <p class="purpose__text" style="top:102px">At træne de vigtigste værktøjer og metoder i praksis gennem konkrete øvelser</p>
    <div class="purpose__strip"></div>
  </section>

  <section class="slide slide--section">
    <svg class="section__frame" viewBox="0 0 245 138">
      <polyline points="37,102 25,102 25,30 130,30" fill="none" stroke="var(--red)" stroke-width="0.8"/>
      <polyline points="130,30 219,30 219,110 188,110" fill="none" stroke="var(--blue)" stroke-width="0.8"/>
      <path d="M22.5 33l2.5-5 2.5 5z" fill="var(--red)"/>
      <path d="M127 27h6l-3 4z" fill="var(--blue)"/>
      <path d="M216 110h6l-3 4z" fill="var(--blue)"/>
      <path d="M44 89h6l-3 4z" fill="var(--blue)"/>
      <path d="M199 114l3-5 3 5z" fill="var(--red)"/>
    </svg>
    <div class="section__title">PLANLÆGNINGSPROCESSEN</div>
  </section>
</body>
</html>
```